Business Card Design Project

We need a redesign of our business card.
We are a Consulting Property Developer called The Selwick Group
Updates

Thank you all for submissions. Just waiting on managment to decide.

Thank you,

Dorinda

Industry/Entity Type

Business

Requirements
Must have
• we like having the SG a focus in the back ground or on the side
Selwick is our company colour

the wording - property development
and - premium accommodation

our website www.selwickgroup.com.au

persons name
title

p: 1300 582914 f: 1300 582917 m: 0419358027
PO Box 2817, Brackenvale Qld 4215
e: admin@selwickgroup.com.au

```html
<!DOCTYPE html>
<html lang="en">
<head>
<meta charset="utf-8">
<title>The Selwick Group – Business Card</title>
<link rel="stylesheet" href="https://fonts.googleapis.com/css2?family=Open+Sans:wght@400&family=Noto+Serif:wght@400&display=swap">
<style>
  :root {
    --backdrop: #2a2a2a;
    --card: #ffffff;
    --maroon: #7d1a20;
    --maroon-dark: #4a070b;
    --maroon-light: #9a2a30;
    --grey-text: #6f6f6f;
    --rule: #b9b9b9;
    --band-grey: #5a5a5a;
    --band-grey-dark: #2f2f2f;
    --silver: #d6d6d6;
    --watermark: #ececec;
  }
  * { box-sizing: border-box; margin: 0; padding: 0; }
  html, body {
    width: 1200px; height: 900px; overflow: hidden;
    background: var(--backdrop);
  }
  .canvas {
    width: 1200px; height: 900px;
    display: flex; flex-direction: column; align-items: center; justify-content: center;
    gap: 28px;
  }
  .card {
    position: relative;
    width: 760px; height: 410px;
    background: var(--card);
    border-radius: 28px;
    overflow: hidden;
  }
  .brand {
    display: flex; align-items: center; gap: 14px;
    font-family: "Open Sans", sans-serif;
    font-weight: 400;
    color: var(--maroon);
    white-space: nowrap;
  }
  .brand-mark { width: 16px; height: 16px; background: var(--maroon); }
  .brand-rule { height: 1px; background: var(--rule); }

  /* Front */
  .watermark {
    position: absolute; right: -70px; top: -90px;
    width: 330px; height: 330px;
    border-radius: 50%;
    background: var(--watermark);
  }
  .card-front .brand { position: absolute; left: 70px; top: 48px; font-size: 42px; }
  .card-front .brand-rule { position: absolute; left: 70px; top: 112px; width: 560px; }
  .contact {
    position: absolute; left: 420px; top: 140px;
    font-family: "Noto Serif", serif;
    font-size: 16px; line-height: 24px;
    color: var(--maroon);
    list-style: none;
  }
  .person { position: absolute; left: 70px; top: 238px; font-family: "Noto Serif", serif; }
  .person-name { font-size: 24px; color: var(--grey-text); }
  .person-title { font-size: 21px; color: var(--maroon); margin-top: 4px; }
  .front-band-edge {
    position: absolute; left: 0; right: 0; bottom: 92px; height: 5px;
    background: linear-gradient(90deg, var(--silver), #8c8c8c 60%, var(--silver));
  }
  .front-band {
    position: absolute; left: 0; right: 0; bottom: 0; height: 92px;
    background: linear-gradient(90deg, var(--maroon-dark), var(--maroon-light) 50%, var(--maroon-dark));
    display: flex; align-items: center; justify-content: center; padding-left: 120px;
  }
  .website {
    font-family: "Noto Serif", serif;
    font-size: 22px; letter-spacing: 0.5px;
    color: #f1e6e6;
  }

  /* Back */
  .card-back .brand { position: absolute; left: 0; right: 0; top: 92px; justify-content: center; font-size: 50px; }
  .card-back .brand-rule { position: absolute; left: 150px; top: 172px; width: 480px; }
  .tagline {
    position: absolute; left: 0; right: 0; top: 190px;
    text-align: center;
    font-family: "Noto Serif", serif;
    font-size: 16px; letter-spacing: 2px; text-transform: uppercase;
    color: var(--grey-text);
  }
  .tagline-divider { color: var(--maroon); margin: 0 10px; }
  .back-line {
    position: absolute; left: 0; right: 0; bottom: 112px; height: 3px;
    background: var(--maroon);
  }
  .back-band {
    position: absolute; left: 0; right: 0; bottom: 0; height: 104px;
    background: linear-gradient(90deg, var(--band-grey-dark), var(--band-grey) 50%, var(--band-grey-dark));
    display: flex; align-items: center; justify-content: center;
  }
  .back-band .website { color: #f2f2f2; }
</style>
</head>
<body>
<main class="canvas">
  <section class="card card-front">
    <div class="watermark" role="img" aria-label="Faint large company monogram decoration"></div>
    <div class="brand"><span class="brand-mark"></span><span>The Selwick Group</span></div>
    <div class="brand-rule"></div>
    <ul class="contact">
      <li>PO Box 2817, Brackenvale Qld 4215</li>
      <li>P : 1300 582914</li>
      <li>F : 1300 582917</li>
      <li>M : 0419358027</li>
      <li>E : admin@selwickgroup.com.au</li>
    </ul>
    <div class="person">
      <p class="person-name">Dorinda Harwell</p>
      <p class="person-title">Title</p>
    </div>
    <div class="front-band-edge"></div>
    <div class="front-band"><span class="website">www.selwickgroup.com.au</span></div>
  </section>

  <section class="card card-back">
    <div class="brand"><span class="brand-mark"></span><span>The Selwick Group</span></div>
    <div class="brand-rule"></div>
    <p class="tagline">Property Development<span class="tagline-divider">|</span>Premium Accommodation</p>
    <div class="back-line"></div>
    <div class="back-band"><span class="website">www.selwickgroup.com.au</span></div>
  </section>
</main>
</body>
</html>
```